Tarvel Ridge LLC

Need Professional Business cards for New Investment Fund

Target Market(s)

High Quality investors

Industry/Entity Type

Financial

Contact Information for Business Card

Phone Number +1 555 284 6193
Name Pavel Orlinsky
Title Fund Manager
email po@FundTarvel.example
Website www.FundTarvel.example

Colors

Designer to choose colors to be used in the design.

Requirements
Must have
• Must have our Logo and all of the above. Must be made so lettering and loge can be raised

```html
<!DOCTYPE html>
<html lang="en">
<head>
<meta charset="utf-8">
<title>Tarvel Ridge LLC – Business Card</title>
<link rel="stylesheet" href="https://fonts.googleapis.com/css2?family=Mulish:wght@400;700&display=swap">
<style>
  :root {
    --card-bg: #ffffff;
    --brand-green: #5bbb46;
    --brand-dark: #434f42;
    --text-grey: #4a4a4a;
    --contact-ink: #3d3d3d;
  }
  html, body {
    margin: 0;
    padding: 0;
    width: 1200px;
    height: 720px;
    overflow: hidden;
    background: var(--card-bg);
  }
  .card {
    position: relative;
    width: 1200px;
    height: 720px;
    background: var(--card-bg);
    font-family: "Mulish", "Century Gothic", sans-serif;
    overflow: hidden;
  }
  .rule {
    position: absolute;
    top: 357px;
    height: 7px;
  }
  .rule--lead {
    left: 0;
    width: 200px;
    background: var(--brand-dark);
  }
  .rule--main {
    left: 200px;
    right: 0;
    background: var(--brand-green);
  }
  .brand {
    position: absolute;
    left: 150px;
    top: 252px;
    display: flex;
    align-items: center;
    gap: 14px;
  }
  .brand__square {
    width: 28px;
    height: 28px;
    background: var(--brand-green);
  }
  .brand__name {
    font-weight: 700;
    font-size: 42px;
    color: var(--brand-dark);
    letter-spacing: 0.5px;
    line-height: 1;
  }
  .person {
    position: absolute;
    left: 578px;
    top: 200px;
  }
  .person__name {
    margin: 0;
    font-weight: 700;
    font-size: 39px;
    color: var(--brand-green);
    line-height: 1.1;
    letter-spacing: 0.3px;
  }
  .person__title {
    margin: 6px 0 0;
    font-weight: 400;
    font-size: 31px;
    color: var(--text-grey);
    line-height: 1.2;
    letter-spacing: 0.5px;
  }
  .contacts {
    position: absolute;
    left: 576px;
    top: 416px;
    margin: 0;
    padding: 0;
    list-style: none;
  }
  .contacts__item {
    display: flex;
    align-items: center;
    height: 43px;
    font-size: 31px;
    color: var(--contact-ink);
    letter-spacing: 0.4px;
  }
  .contacts__icon {
    width: 28px;
    height: 28px;
    margin-right: 20px;
    flex: none;
    fill: var(--contact-ink);
  }
  .contacts__icon--outline {
    fill: none;
    stroke: var(--contact-ink);
    stroke-width: 1.8;
  }
</style>
</head>
<body>
  <main class="card">
    <div class="rule rule--lead"></div>
    <div class="rule rule--main"></div>

    <div class="brand">
      <span class="brand__square"></span>
      <span class="brand__name">Tarvel Ridge</span>
    </div>

    <section class="person">
      <h1 class="person__name">Pavel Orlinsky</h1>
      <p class="person__title">Fund Manager</p>
    </section>

    <ul class="contacts">
      <li class="contacts__item">
        <svg class="contacts__icon" viewBox="0 0 24 24" aria-hidden="true">
          <path d="M6.6 2.5c.6-.3 1.2 0 1.5.5l2 3.5c.3.5.2 1.1-.2 1.5L8.3 9.4c1 2.4 3.5 4.9 6.3 6.3l1.4-1.6c.4-.4 1-.5 1.5-.2l3.5 2c.5.3.8.9.5 1.5l-1 2.4c-.3.7-1 1.1-1.8 1C10 19.9 4.1 14 3.2 5.3c-.1-.8.3-1.5 1-1.8z"/>
        </svg>
        <span>+1 555 284 6193</span>
      </li>
      <li class="contacts__item">
        <svg class="contacts__icon" viewBox="0 0 24 24" aria-hidden="true">
          <path d="M12 2 2 9v11h20V9zm0 2.4 7.6 5.3L12 14 4.4 9.7z"/>
        </svg>
        <span>po@FundTarvel.example</span>
      </li>
      <li class="contacts__item">
        <svg class="contacts__icon contacts__icon--outline" viewBox="0 0 24 24" aria-hidden="true">
          <circle cx="12" cy="12" r="9.5"/>
          <ellipse cx="12" cy="12" rx="4" ry="9.5"/>
          <line x1="2.5" y1="12" x2="21.5" y2="12"/>
          <line x1="4" y1="7" x2="20" y2="7"/>
          <line x1="4" y1="17" x2="20" y2="17"/>
        </svg>
        <span>www.FundTarvel.example</span>
      </li>
    </ul>
  </main>
</body>
</html>
```